Corvane Networks web design

Corvane is an Internet Service Provider bringing high-speed service to homes and businesses. Our principal market target is rural areas of West Michigan, but we intend to expand rapidly. We need a website to market our services, facilitate online ordering, customer support and communicate with our customers.

I will upload a draft outline of the content we hope to include in the website.

We compete directly with Halberd Communications, Lumetra, Dravix and Kelwick communications to bring Internet service to homes and businesses in our coverage area.

Our primary values include:

1. Unlike our competitors, we do not require long term contractors or service bundles; There are no termination fees, for example. All services are sold on a recurring 1-month agreement term.
2. Unlike other wireless (mobile) providers, we do not limit downloads or uploads with bit/byte buckets
3. We provide service to areas ignored by the larger carriers - Rural areas in Michigan that lack options for broadband are prime targets for Corvane to cover.
4. Unlike other wireless ISP's, we utilize licensed FCC spectrum. We do not use unlicensed/free frequencies, providing us an advantage for reliability and stability.
Updates

So many wonderful designs, thank you very much for all your hard work. We are evaluating all our favorite designs and plan to make a selection in the next 2 days. I will be in touch with you to request revisions if necessary or further refinements.  Thank you again for your efforts on this project.

Target Market(s)

Our target market is home Internet users. however, that does not mean that our users are "high tech" oriented - they are just normal mom's and pop's who buy Internet for home use. The site should be easy to navigate and communicate our message of speed, value, reliability and facilitate simple product ordering.

Industry/Entity Type

Internet

Requirements
Must have
• Our phone number should be prominently displayed 1-844-7NU-LINK
• Our logo is uploaded in the attachments.
• Design for desktop and mobile devices.
Nice to have
• The most modern of web design trends. Such as a design that facilitates parallax scrolling effects rather than lots of individual pages.
• Stock artwork communicating our values of speed and reliability.

```html
<!DOCTYPE html>
<html lang="en">
<head>
<meta charset="utf-8">
<title>Corvane Networks</title>
<link href="https://fonts.googleapis.com/css2?family=Open+Sans:wght@300;400;600;700&display=swap" rel="stylesheet">
<style>
:root{
  --orange:#ff7a00;
  --charcoal:#4a4a4a;
  --header:#555555;
  --dark:#1f1f1f;
  --band:#505050;
  --page:#e4e4e4;
  --card:#e9e9e9;
  --text:#333;
  --muted:#777;
  --sky:#0aa4e0;
  --white:#fff;
}
*{margin:0;padding:0;box-sizing:border-box}
html,body{width:759px;height:1200px;overflow:hidden}
body{position:relative;background:var(--page);font-family:'Open Sans',sans-serif;color:var(--text)}
.abs{position:absolute}
.header{left:52px;top:0;width:655px;height:87px;background:var(--header)}
.brand{left:31px;top:42px;color:var(--orange);font-weight:700;font-size:17px;letter-spacing:1px;line-height:1}
.brand small{display:block;font-size:8px;letter-spacing:5px;margin-top:3px}
.phone-icon{left:526px;top:13px}
.enquiry{left:543px;top:11px;color:#eee;font-size:8px;line-height:1.2}
.enquiry b{display:block;color:var(--orange);font-weight:400;font-size:11.5px}
.nav{left:214px;top:68px;font-size:8px;font-weight:600;color:#fff}
.nav span{position:absolute;white-space:nowrap}
.search{left:502px;top:65px;width:123px;height:17px;background:#fff;font-size:7px;font-style:italic;color:#999;padding:4px 9px}
.hero{left:52px;top:90px;width:655px;height:259px;background:linear-gradient(120deg,#8a8077 0%,#c9b8a4 30%,#5f4f44 60%,#9aa3a8 100%)}
.caption{left:52px;top:214px;width:296px;height:91px;background:rgba(40,40,40,.6)}
.caption h1{position:absolute;left:27px;top:10px;font-size:20px;font-weight:600;color:#fff;line-height:1}
.caption h2{position:absolute;left:26px;top:32px;font-size:13.5px;font-weight:400;color:var(--orange);white-space:nowrap}
.caption p{position:absolute;left:27px;top:51px;font-size:10.5px;color:#fff;line-height:1.5}
.caption p b{font-size:14px;font-weight:400}
.dot{width:8px;height:8px;border-radius:50%;background:#444;top:324px}
.dot.on{background:var(--orange);border:1.5px solid #fff}
.panel{left:52px;top:366px;width:655px;height:644px;background:#fff}
.intro h3{font-size:17.5px;font-weight:400;color:#333;line-height:1.05}
.intro h3 em{font-style:normal;color:var(--orange);display:block}
.intro p{font-size:7.5px;color:var(--muted);line-height:1.7;margin-top:9px;width:280px}
.intro ul{list-style:none;margin-top:10px}
.intro li{font-size:7.5px;font-weight:600;line-height:13px;padding-left:14px;position:relative}
.intro li:before{content:"";position:absolute;left:0;top:3px;border-left:6px solid var(--orange);border-top:3.5px solid transparent;border-bottom:3.5px solid transparent}
.intro .tag{font-size:9.5px;color:#444;margin-top:8px}
.intro .tag span{color:var(--orange)}
.divider{left:379px;top:410px;width:1px;height:184px;background:#ccc}
.news-title{left:413px;top:408px;font-size:18px;color:#333}
.news-title span{color:var(--orange)}
.news{left:413px;width:264px;height:75px;background:var(--card);padding:9px 14px 0 21px}
.news h5{font-size:8px;font-weight:600;color:#555;display:flex;align-items:center;gap:5px}
.news p{font-size:7.5px;color:var(--muted);line-height:1.3;margin-top:9px;text-align:justify}
.promo{top:625px;height:207px;background:var(--orange);color:#fff;padding:18px 22px 0 19px}
.promo h4{font-size:17px;font-weight:600}
.promo ul{list-style:none;margin-top:14px}
.promo li{font-size:7.5px;line-height:13px;padding-left:14px;position:relative;margin-bottom:13px;text-align:justify}
.promo li:before{content:"";position:absolute;left:0;top:4px;width:5px;height:5px;border-radius:50%;background:#fff}
.feed{top:858px;height:134px;color:#fff;padding:11px 12px}
.feed h6{font-size:7.5px;font-weight:700;display:flex;align-items:center;gap:6px}
.feed h6:after{content:"";flex:1;height:1px;background:rgba(255,255,255,.6)}
.item{display:flex;gap:9px;margin-top:9px;font-size:7.5px;line-height:1.3}
.avatar{flex:none;width:38px;height:38px;border-radius:50%;border:2px solid #fff;background:linear-gradient(#b9a89a,#6f625a)}
.thumb{flex:none;width:32px;height:34px;background:linear-gradient(#c7c2bb,#6d6760)}
.hl{color:var(--orange)}
.more{position:absolute;right:22px;bottom:10px;font-size:7.5px}
.band{left:0;top:1010px;width:759px;height:43px;background:var(--band);color:#fff;font-size:9.5px}
.foot{left:0;top:1053px;width:759px;height:147px;background:var(--dark);color:#aaa;font-size:7.5px}
.foot h6{color:var(--orange);font-size:9.5px;font-weight:600;margin-bottom:9px}
.foot .list{line-height:10px}
.vline{width:1px;background:#333}
.social{width:20px;height:20px;border-radius:50%;background:#777;top:1170px}
</style>
</head>
<body>
<header class="abs header">
  <div class="abs brand">CORVANE<small>NETWORKS</small></div>
  <svg class="abs phone-icon" width="12" height="19" viewBox="0 0 12 19"><rect x="1" y="1" width="10" height="17" rx="1.5" fill="none" stroke="#fff" stroke-width="1.5"/><rect x="3" y="3.5" width="6" height="10" fill="#fff"/></svg>
  <div class="abs enquiry">call us for enquiries<b>844-7NU-LINK</b></div>
  <nav class="abs nav">
    <span style="left:0;color:var(--orange)">HOME</span>
    <span style="left:48px">SERVICE PLANS</span>
    <span style="left:130px">COVERAGE MAP</span>
    <span style="left:220px">ABOUT US</span>
  </nav>
  <div class="abs search">web search
    <svg class="abs" style="right:6px;top:3px" width="11" height="11" viewBox="0 0 11 11"><circle cx="4.5" cy="4.5" r="3.3" fill="none" stroke="#ff7a00" stroke-width="1.6"/><line x1="7" y1="7" x2="10" y2="10" stroke="#ff7a00" stroke-width="2"/></svg>
  </div>
</header>

<section class="abs hero" role="img" aria-label="Photo of two young people smiling while looking at a tablet"></section>
<div class="abs caption">
  <h1>WHY WE’RE BETTER?</h1>
  <h2>Faster Speed, No Limits, More Value</h2>
  <p>For more details Call us<br><b>844-7NU-LINK</b></p>
</div>
<div class="abs dot on" style="left:342px"></div>
<div class="abs dot" style="left:365px"></div>
<div class="abs dot" style="left:387px"></div>
<div class="abs dot" style="left:410px"></div>

<main class="abs panel"></main>
<section class="abs intro" style="left:82px;top:410px">
  <h3>West Michigan’s<em>Best Internet Service</em></h3>
  <p>Corvane Networks is a Michigan-based company providing high-speed Internet services to West Michigan homes and businesses.</p>
  <ul>
    <li>100% Satisfaction Guaranteed</li>
    <li>Honest Pricing, No Hidden Fees</li>
    <li>No Long Term Contracts</li>
    <li>No Phone Line or Cable TV required</li>
    <li>Fast, Superior Performance for your home and business</li>
    <li>Interference-Free FCC Licensed 4G Coverage</li>
  </ul>
  <div class="tag"><span>Corvanelink</span> delivers West Michigan's Best Internet Service</div>
</section>
<div class="abs divider"></div>

<div class="abs news-title">Latest <span>news</span></div>
<svg class="abs" style="left:540px;top:424px" width="12" height="7"><polyline points="1,6 6,1 11,6" fill="none" stroke="#333" stroke-width="1.2"/></svg>
<article class="abs news" style="top:436px">
  <h5><svg width="12" height="12"><rect x="1" y="1" width="10" height="10" fill="none" stroke="#555"/><line x1="3" y1="4" x2="9" y2="4" stroke="#555"/><line x1="3" y1="6.5" x2="9" y2="6.5" stroke="#555"/><line x1="3" y1="9" x2="9" y2="9" stroke="#555"/></svg>December 14, 2014</h5>
  <p>Corvane Networks is a Michigan-based company providing high-speed Internet services to West Michigan homes and businesses.</p>
</article>
<article class="abs news" style="top:518px">
  <h5><svg width="12" height="12"><rect x="1" y="1" width="10" height="10" fill="none" stroke="#555"/><line x1="3" y1="4" x2="9" y2="4" stroke="#555"/><line x1="3" y1="6.5" x2="9" y2="6.5" stroke="#555"/><line x1="3" y1="9" x2="9" y2="9" stroke="#555"/></svg>December 19, 2014</h5>
  <p>Corvane Networks is a Michigan-based company providing high-speed Internet services to West Michigan homes and businesses.</p>
</article>
<svg class="abs" style="left:540px;top:600px" width="12" height="7"><polyline points="1,1 6,6 11,1" fill="none" stroke="#333" stroke-width="1.2"/></svg>

<section class="abs promo" style="left:82px;width:293px">
  <h4>Why Corvane?</h4>
  <ul>
    <li>No Download Limits! Corvane doesn’t charge you more when you use more</li>
    <li>No Cancellation Fees! All services are sold on 1-month terms, there are no contract minimums and never a cancellation fee.</li>
    <li>FCC Licensed reliability. Corvane 4G utilizes the latest wireless technologies using FCC licensed frequencies. Unlike other West Michigan ISP’s, our signals never fade. Enjoy stable and reliable Internet service.</li>
  </ul>
</section>
<section class="abs promo" style="left:385px;width:292px">
  <h4>Buy Local</h4>
  <ul>
    <li>Corvane is Local! We’re a locally owned and operated business. All of our staff live and work in Michigan. We invest in our local community because we live it- just like you!</li>
    <li>Best Value, Best for You! Unlike cable and phone companies, we don’t require you to buy everything from us. We offer the best value Internet service, and only what you want, no “bundles” required.</li>
  </ul>
</section>

<section class="abs feed" style="left:82px;width:292px;background:var(--charcoal)">
  <h6>LATES BLOG POSTS</h6>
  <div class="item"><div class="avatar" role="img" aria-label="Blog author portrait"></div><p><span class="hl">Corvane Networks is a Michigan-based</span> company providing high-speed Internet services to West Michigan homes and businesses.</p></div>
  <div class="item" style="margin-top:5px"><div class="avatar" role="img" aria-label="Blog author portrait"></div><p>Corvane Networks is a Michigan-based company providing high-speed Internet <span class="hl">services to West Michigan</span> homes and businesses.</p></div>
  <span class="more hl">View all blogs</span>
</section>
<section class="abs feed" style="left:385px;width:291px;background:var(--sky)">
  <h6>LATES TWEETS</h6>
  <div class="item"><div class="thumb" role="img" aria-label="Profile photo"></div><p><b style="font-weight:600">Maren Holt</b><br><b style="font-weight:600">Corvane Networks is a Michigan-based</b> company providing high-speed Internet services to West Michigan...</p></div>
  <div class="item" style="margin-top:5px"><div class="thumb" role="img" aria-label="Profile photo"></div><p><b style="font-weight:600">Devin Arlo</b><br><b style="font-weight:600">Corvane Networks is a Michigan-based</b> company providing high-speed Internet services to West Michigan...</p></div>
  <span class="more">View new tweets</span>
</section>

<footer>
  <div class="abs band">
    <svg class="abs" style="left:82px;top:10px" width="22" height="22"><rect width="22" height="22" rx="3" fill="#777"/><path d="M7 5c1 0 2 3 1.5 4l-1 1c1 2 2 3 4 4l1-1c1-.5 4 .5 4 1.5 0 2-2 3-3 3C9 17 5 13 5 8c0-1 1-3 2-3z" fill="#fff"/></svg>
    <span class="abs" style="left:112px;top:14px">844-7NU-LINK | 517-555-0142</span>
    <svg class="abs" style="left:270px;top:10px" width="22" height="22"><rect width="22" height="22" rx="3" fill="#777"/><rect x="4" y="6" width="14" height="10" fill="none" stroke="#fff"/><polyline points="4,6 11,12 18,6" fill="none" stroke="#fff"/></svg>
    <span class="abs" style="left:300px;top:12px;font-size:8.5px">support@corvanelink.com</span>
    <span class="abs" style="left:541px;top:15px;font-size:8px;color:#bbb">Proud to live and work in Michigan!</span>
  </div>
  <div class="abs foot">
    <div class="abs" style="left:82px;top:16px"><h6>QUICK LINKS</h6><div class="list">Service Plans<br>Coverage Map<br>WhoIs Corvane<br>Company Blog<br>Customer Support<br>Account Management</div></div>
    <div class="abs vline" style="left:189px;top:0;height:109px"></div>
    <div class="abs" style="left:212px;top:16px"><h6>SUPPORT STAFF HOURS</h6><div class="list">Weekdays 7am to 10pm<br>Weekends 8am to 5pm<br>Holiday scheduling varies</div></div>
    <div class="abs vline" style="left:342px;top:0;height:109px"></div>
    <div class="abs" style="left:560px;top:40px"><h6 style="margin-bottom:7px">CORVANE NETWORKS, LLC</h6><div class="list" style="font-size:6.5px;line-height:9px">1187 BIRCHLINE AVENUE<br>EAST LANSING, MI 48823</div></div>
    <div class="abs" style="left:0;top:109px;width:759px;height:1px;background:#333"></div>
    <span class="abs" style="left:82px;top:118px;color:#666">© Copyright 2014 . All rights reserved to Corvane Networks, LLC</span>
  </div>
  <div class="abs social" style="left:606px" aria-label="Social link"></div>
  <div class="abs social" style="left:631px" aria-label="Social link"></div>
  <div class="abs social" style="left:656px" aria-label="Social link"></div>
</footer>
</body>
</html>
```